Дизайн этикетки и упаковки лечебной косметики
Задание на дизайн
Приоритеты объектов в упаковке
Зонтичная марка, Вид продукта, Название продукта
Опишите свою организацию или продукт и целевую аудиторию
Продукция представляет собой линейку новой лечебной косметики (космецевтики) под брендом (зонтичная марка) «Dr. Vok», направленную на решение проблем при повреждениях кожи (раны, ссадины, незначительные ожоги, угревая сыпь в стадии воспаления и после вскрытия прыщей) и слизистой оболочки рта (воспаления, раны, укрепление десен и др., после стоматологических операций и имплантаций), а также после бритья и косметических манипуляций (чистка лица, пилинг, депиляция, татуаж, мезотерапия, бритье, маникюр, педикюр и др.). Эффект продуктов обусловлен инновационным комплексом «Zentrava» и дополнен веществами, способствующими восстановлению и регенерации кожи и слизистой.
Название продуктов:
- Бальзам для полости рта Заживление + Регенерация
- Сыворотка для проблемной и поврежденной кожи Заживление + Регенерация
Целевая аудитория сыворотки для кожи – преимущественно женский пол от 16 до 40, имеющие проблемы с кожей, а также женщины от 35 и старше, для которых важна забота о себе и регулярно делающие косметические манипуляции с нарушением кожных покровов (пилинг, депиляция и т.д.).
Целевая аудитория бальзама – преимущественно люди обоих полов, от 30 и старше.
Ценовой сегмент – средний.
Продукция на рынке новая. Продажи в первое время – через маркетплейсы. Выпускается во флаконах коричневого цвета с черной крышкой по 50 мл.
ЗАДАЧА: разработать запоминающийся, привлекающий внимание, «продающий» дизайн упаковки и этикетки для продукции, ассоциирующейся со здоровьем, надежностью, качеством, инновационностью, современностью.
Вся информация тут: https://files.quorvani-docs.net/d/8Kx4TqWbLp2RzN7vYeHs3JdUcGa/view?share=open&uid=552901873460218837412&fmt=full
К предложенным образцам не обязательно привязываться, интересней предложить собственную концепцию
Комментарии и пожелания для дизайнеров
Дизайн коробок и этикеток должен быть выполнен в одном стиле, но каждый продукт должен быть узнаваем за счет цвета и/или дополнительных элементов, например, рисунка, графики. Цветовая гамма – на усмотрение дизайнера. Желательно не менее трех цветов.
Коробка – четыре одинаковые плоскости, верх (крышка), дно. Основные плоскости: высота – 119 мм, ширина – 38 мм. Крышка и дно: 38×38 мм
Этикетка круговая, может быть разделена на несколько частей. Пропорции деления определяются дизайном.
Этикетка сыворотка: высота – 41 мм, длина – 114 мм
Этикетка бальзам: высота – 59 мм, длина – 101 мм
Выпускается во флаконах коричневого цвета с черной крышкой по 50 мл.
Название бренда выполняется в виде подписи «Sincerely, Dr. Vok». Подпись должна быть выполнена как бы «от руки», расположена внизу этикетки и коробки, не должна превалировать над остальными элементами, но быть хорошо видимой. Возможно, под небольшим уклоном.
Главными элементами должны быть: вид продукции (бальзам, сыворотка), слоган Заживление + Регенерация и указание активного комплекса Zentrava.
Шрифты подбирает/разрабатывает дизайнер самостоятельно.
Дополнительные требования тут: https://files.quorvani-docs.net/d/8Kx4TqWbLp2RzN7vYeHs3JdUcGa/view?share=open&uid=552901873460218837412&fmt=full

```html
<!DOCTYPE html>
<html lang="ru">
<head>
<meta charset="utf-8">
<title>Бальзам для полости рта — этикетка и коробка</title>
<link rel="stylesheet" href="https://fonts.googleapis.com/css2?family=PT+Sans:wght@700&family=PT+Serif:wght@400;700&display=swap">
<style>
  :root {
    --canvas: #eceef1;
    --paper: #ffffff;
    --ink: #1f2430;
    --ink-soft: #4a5160;
    --navy: #243a5e;
    --band-light: #dfe8f3;
    --band-mid: #bcd0e8;
    --stripe: #9fb8d9;
    --accent-red: #d8222a;
    --edge: #d6dbe2;
  }
  * { box-sizing: border-box; margin: 0; padding: 0; }
  html, body { width: 1200px; height: 915px; overflow: hidden; }
  body {
    background: var(--canvas);
    font-family: "PT Serif", Georgia, serif;
    color: var(--ink);
    position: relative;
  }

  /* ---------- Bottle label (flat) ---------- */
  .label {
    position: absolute;
    left: 70px; top: 300px;
    width: 540px; height: 316px;
    background: var(--paper);
    border: 1px solid var(--edge);
    display: flex; flex-direction: column;
  }
  .label__head { padding: 38px 0 0; text-align: center; }
  .product-type { font-weight: 700; letter-spacing: 1px; }
  .label .product-type { font-size: 36px; line-height: 1; }
  .product-use { font-size: 17px; color: var(--ink-soft); margin-top: 6px; }
  .label__band {
    margin-top: 26px;
    height: 92px;
    background: linear-gradient(180deg, var(--band-mid) 0%, var(--band-light) 100%);
    display: flex; flex-direction: column; align-items: center; justify-content: center;
  }
  .complex-name {
    font-family: "PT Sans", Arial, sans-serif;
    font-weight: 700;
    color: var(--navy);
  }
  .label .complex-name { font-size: 34px; line-height: 1; }
  .slogan { display: flex; align-items: center; gap: 10px; font-size: 20px; margin-top: 8px; }
  .plus { color: var(--accent-red); font-family: "PT Sans", Arial, sans-serif; font-weight: 700; line-height: 1; }
  .slogan .plus { font-size: 34px; }
  .label__foot {
    flex: 1; position: relative;
    display: flex; align-items: center; justify-content: center;
  }
  .volume { font-size: 19px; }
  .signature { font-family: "PT Serif", Georgia, serif; font-weight: 400; color: var(--ink); line-height: 1.1; }
  .label .signature { position: absolute; right: 26px; top: 16px; font-size: 17px; text-align: left; }

  /* ---------- Box panels (flat) ---------- */
  .box-panel {
    position: absolute; top: 100px;
    width: 228px; height: 712px;
    background: var(--paper);
    border: 1px solid var(--edge);
  }
  .box-panel::before, .box-panel::after {
    content: ""; position: absolute; left: 0; right: 0; height: 8px; background: var(--stripe);
  }
  .box-panel::before { top: 16px; }
  .box-panel::after { bottom: 16px; }

  .box-front { left: 664px; text-align: center; }
  .box-front .front__head { padding-top: 86px; }
  .box-front .product-type { font-size: 24px; }
  .box-front .product-use { font-size: 14px; margin-top: 4px; }
  .front__band {
    margin-top: 60px; height: 118px;
    background: linear-gradient(180deg, var(--band-mid) 0%, var(--band-light) 100%);
    display: flex; align-items: center; justify-content: center;
    font-size: 19px; line-height: 1.25; color: var(--ink);
  }
  .box-front .complex-name { font-size: 24px; margin-top: 14px; }
  .front__slogan { margin-top: 46px; font-size: 17px; line-height: 1.3; }
  .front__slogan .plus { display: block; font-size: 40px; margin: 2px 0; }
  .box-front .signature { position: absolute; left: 118px; top: 520px; font-size: 16px; text-align: left; }
  .box-front .volume { position: absolute; left: 0; right: 0; bottom: 64px; font-size: 14px; }

  .box-side { left: 904px; padding: 86px 22px 0; }
  .box-side .product-type { font-size: 21px; text-align: center; }
  .box-side .product-use { font-size: 12px; text-align: center; margin-top: 3px; }
  .side__text { margin-top: 28px; font-size: 10.5px; line-height: 1.5; color: var(--ink-soft); }
  .side__text ul { list-style: none; }
  .side__text p + p, .side__text ul + p { margin-top: 14px; }
  .side__note { margin-top: 64px !important; }
</style>
</head>
<body>

  <section class="label" aria-label="Этикетка флакона">
    <div class="label__head">
      <h1 class="product-type">БАЛЬЗАМ</h1>
      <p class="product-use">для полости рта</p>
    </div>
    <div class="label__band">
      <p class="complex-name">Zentrava</p>
      <p class="slogan">Заживление <span class="plus">+</span> Регенерация</p>
    </div>
    <div class="label__foot">
      <p class="volume">50 мл</p>
      <p class="signature">Sincerely,<br>Dr. Vok</p>
    </div>
  </section>

  <section class="box-panel box-front" aria-label="Лицевая сторона коробки">
    <div class="front__head">
      <h2 class="product-type">БАЛЬЗАМ</h2>
      <p class="product-use">для полости рта</p>
    </div>
    <div class="front__band">
      <p>На основе<br>инновационного<br>активного комплекса</p>
    </div>
    <p class="complex-name">Zentrava</p>
    <p class="front__slogan">Заживление<span class="plus">+</span>Регенерация</p>
    <p class="signature">Sincerely,<br>Dr. Vok</p>
    <p class="volume">50 мл</p>
  </section>

  <section class="box-panel box-side" aria-label="Боковая сторона коробки">
    <h2 class="product-type">БАЛЬЗАМ</h2>
    <p class="product-use">для полости рта</p>
    <div class="side__text">
      <p>Способствует заживлению и регенерации:</p>
      <ul>
        <li>- при воспалительных процессах на слизистой рта;</li>
        <li>- при реабилитации после имплантации и удаления;</li>
        <li>- при кровоточивости десен;</li>
        <li>- при частых или хронических стоматитах;</li>
        <li>- восстановлению при гингивитах, пародонтитах, пародонтозе;</li>
        <li>- для укрепления десен.</li>
      </ul>
      <p>Не содержит спирт, парабены, красители. Не тестируется на животных.</p>
      <p class="side__note">Назначение и способ применения смотри листовку-вкладыш.</p>
    </div>
  </section>

</body>
</html>
```